Client website

Our designer we were working with had some personal things come up and was unable to finish the design for the site.

We have a .psd file started, and will be attaching it to the project.

Reason: I still want to polish the designs with the current designer and allow more designers the opportunity to participate.

Reason: I'm extending the deadline for another day to give everyone enough time for the final changes our client wants.

I'm trying to extend the deadline so we can get one last set of comps in for my client.  Could everyone message me and let me know how much time they need to do the final tweaks?

Reason: Hey everyone.  I've been sick the last 3 days and I haven't been able to provide feedback on designs.  I'm extending just a few more days so I can catch up here.  Thanks everyone for your patience.

Adults in United States aged 25 to 60 that handle the household budgets and maintenance.

• 1) We need 2 pages. 1 page for flood restoration, 1 page for carpet cleaning

2) The 1-800-# must be the focal point of the website for both pages. People are mostly looking to contact someone ASAP to get them out to their house when flooding occurs.

3) We''re going to have a slide show area to high-light different sub-services offered for each page.

4) We really want a pagenest / lumora feed area. We''re going to use pagenest for special offers, and lumora for weather updates. The pagenest feed is going to be on the carpet cleaning page. The lumora feed is going to be on the flood page.

5) We want an SEO text sections near the bottom.

6) The very bottom will link to the privacy policy and user agreement as well as company name and copyright details.

We really want to stick to the say "theme" that our first designer started with.
• I'm not a designer, so if you think something looks better somewhere, or something can be eliminated, or something can be enhanced, but all means, let us know.

```html
<!DOCTYPE html>
<html lang="en">
<head>
<meta charset="utf-8">
<title>Clearwell – Water &amp; Fire Damage Restoration</title>
<link href="https://fonts.googleapis.com/css2?family=Arimo:wght@400;700&family=Ubuntu:wght@400;500;700&display=swap" rel="stylesheet">
<style>
:root{
  --page-bg:#1b3142;
  --page-dot:#24405a;
  --navy:#0d2a45;
  --sky-top:#ffffff;
  --sky-bottom:#d6ecf9;
  --nav-top:#1e7cc4;
  --nav-bottom:#0c5596;
  --nav-active:#a9d8fb;
  --body-top:#2a8fd2;
  --body-bottom:#36a7e0;
  --panel:rgba(255,255,255,.12);
  --panel-line:rgba(255,255,255,.28);
  --link:#cfe9ff;
  --white:#ffffff;
  --brand-green:#1aa33a;
  --brand-blue:#1b6fc0;
}
*{box-sizing:border-box;margin:0;padding:0}
html,body{width:1200px;height:1138px;overflow:hidden}
body{
  position:relative;
  background:var(--page-bg);
  background-image:radial-gradient(var(--page-dot) 1.2px,transparent 1.6px);
  background-size:8px 8px;
  font-family:"Ubuntu",sans-serif;
  color:var(--white);
}
.site{position:absolute;left:113px;top:23px;width:975px;height:1049px;border-radius:12px;overflow:hidden;
  background:linear-gradient(var(--body-top),var(--body-bottom));}
.header{position:absolute;left:0;top:0;width:975px;height:241px;
  background:linear-gradient(180deg,var(--sky-top) 0%,var(--sky-bottom) 100%);}
.splash{position:absolute;left:180px;top:60px;width:560px;height:150px;border-radius:50%;
  background:radial-gradient(ellipse at center,rgba(120,180,230,.45),rgba(200,230,250,0) 70%);}
.brand{position:absolute;left:34px;top:170px;}
.brand-mark{position:absolute;left:40px;top:-150px;width:140px;height:140px;border-radius:50%;background:var(--brand-blue);}
.brand-name{font-family:"Ubuntu",sans-serif;font-weight:700;font-size:40px;color:var(--brand-green);letter-spacing:1px;line-height:1}
.brand-tag{font-size:13px;color:var(--brand-blue);font-variant:small-caps;letter-spacing:.5px;margin-top:4px;padding-left:11px}
.call{position:absolute;left:633px;top:8px;width:334px;height:90px;border-radius:10px;
  background:rgba(255,255,255,.55);border:1px solid rgba(255,255,255,.8);padding:14px 0 0 20px;color:var(--navy);font-family:"Arimo",sans-serif;font-weight:700}
.call-label{font-size:23px;line-height:1}
.call-number{font-size:38px;line-height:1.05;letter-spacing:-.5px}
.nav{position:absolute;left:0;top:241px;width:975px;height:46px;
  background:linear-gradient(var(--nav-top),var(--nav-bottom));display:flex;align-items:center;padding-left:54px;
  border-bottom:1px solid rgba(255,255,255,.2)}
.nav a{color:var(--white);text-decoration:none;font-weight:700;font-size:16px}
.nav a.active{color:var(--nav-active);font-weight:500}
.nav .sep{width:1px;height:11px;background:rgba(255,255,255,.7);margin:0 22px}
.slider{position:absolute;left:19px;top:302px;width:937px;height:232px;border-radius:6px;overflow:hidden;border:2px solid rgba(160,215,250,.8)}
.slide-photo{position:absolute;inset:0;background:linear-gradient(90deg,#d9ddd2 0%,#b9b9a5 45%,#7d6a55 70%,#5b4a3c 100%)}
.slide-photo::after{content:"";position:absolute;left:0;right:0;bottom:0;height:110px;background:linear-gradient(rgba(140,150,150,.3),rgba(70,80,80,.7))}
.caption{position:absolute;left:0;bottom:0;width:100%;height:55px;background:rgba(20,28,34,.82);padding:13px 0 0 19px}
.caption strong{display:block;font-size:11.5px;font-weight:700}
.caption p{font-size:11px;margin-top:2px}
.dots{position:absolute;right:22px;bottom:20px;display:flex;gap:11px}
.dots span{width:10px;height:10px;border-radius:50%;background:#f2f2f2}
.dots span.on{background:#2a9be3}
.feed{position:absolute;top:609px;width:463px;height:269px;border-radius:6px;background:var(--panel);border:1px solid var(--panel-line);padding:48px 10px 0 10px}
.feed-title{position:absolute;top:-34px;left:147px;font-family:"Arimo",sans-serif;font-weight:700;font-size:24px;text-shadow:0 1px 3px rgba(0,40,80,.6)}
.feed-badge{position:absolute;top:-52px;left:22px;width:112px;height:80px;border-radius:10px;background:linear-gradient(#e9f4fd,#9fc9ee);transform:skewX(-8deg);box-shadow:0 3px 6px rgba(0,0,0,.3)}
.feed.right .feed-title{left:122px}
.feed.right .feed-badge{width:86px;left:20px}
.post{font-size:10.5px;line-height:14px;margin-bottom:8px}
.post p{height:auto}
.meta{display:flex;align-items:center;margin-top:10px;font-weight:700;font-size:11.5px;height:20px}
.meta .user{color:var(--link);margin-left:4px}
.meta .bar{margin:0 8px;font-weight:400}
.btn{margin-left:8px;height:20px;padding:0 7px;border-radius:3px;background:#eef3f8;border:1px solid #b9c9d8;color:#3b5a7a;font-size:11px;font-weight:400;line-height:18px}
.count{margin-left:5px;width:34px;height:20px;background:#fff;border:1px solid #b9c9d8;border-radius:3px;color:#333;font-size:11px;font-weight:400;text-align:center;line-height:18px}
.footer-nav{position:absolute;left:0;top:916px;width:975px;height:133px;border-top:1px solid rgba(255,255,255,.3)}
.footer-head{height:30px;border-bottom:1px solid rgba(255,255,255,.25);background:rgba(255,255,255,.05)}
.footer-col{position:absolute;top:0;height:133px}
.footer-col h4{font-size:11.5px;font-weight:700;height:30px;line-height:30px}
.footer-col ul{list-style:none;margin-top:6px}
.footer-col li{font-size:10.5px;line-height:18px;padding-left:12px;position:relative}
.footer-col li::before{content:"";position:absolute;left:0;top:8px;width:3px;height:3px;background:var(--link)}
.divider{position:absolute;top:30px;width:1px;height:90px;background:rgba(255,255,255,.18)}
.copyright{position:absolute;top:1100px;width:1200px;text-align:center;font-size:10px}
</style>
</head>
<body>
<div class="site">
  <header class="header">
    <div class="splash" role="img" aria-label="Flowing water splash illustration"></div>
    <div class="brand">
      <div class="brand-mark"></div>
      <div class="brand-name">CLEARWELL</div>
      <div class="brand-tag">Water &amp; Fire Damage Restoration</div>
    </div>
    <div class="call">
      <div class="call-label">CALL US</div>
      <div class="call-number">1-800-555-0142</div>
    </div>
  </header>
  <nav class="nav">
    <a class="active" href="#">HOME</a><span class="sep"></span>
    <a href="#">ABOUT</a><span class="sep"></span>
    <a href="#">SERVICES</a><span class="sep"></span>
    <a href="#">FAQ</a><span class="sep"></span>
    <a href="#">CONTACT</a>
  </nav>
  <section class="slider">
    <div class="slide-photo" role="img" aria-label="Photo of flooded living rooms with water covering the floor"></div>
    <div class="caption">
      <strong>Lorem ipsum dolor sit amet, consectetur adipiscing elit.</strong>
      <p>Praesent leo elit, condimentum at fermentum nec, aliquam sit amet diam. Sed egestas aliquet sapien.</p>
    </div>
    <div class="dots"><span class="on"></span><span></span><span></span><span></span><span></span></div>
  </section>

  <section class="feed" style="left:20px">
    <div class="feed-badge"></div>
    <h2 class="feed-title">Find us on pagenest</h2>
    <div class="post"><p>Lorem ipsum dolor sit amet, consectetur adipiscing elit. Sed quis ante felis. Donec porta arcu vehicula purus hendrerit interdum. Suspendisse lacus magna ullamcorper ut aliquet rutrum</p>
      <div class="meta">Posted by: <span class="user">username details</span><span class="bar">|</span>2 hrs ago<span class="bar">|</span><span class="btn">Like</span></div></div>
    <div class="post" style="margin-top:20px"><p>Curabitur laoreet, elit in tincidunt condimentum, massa tortor adipiscing nisl, non condimentum orci nunc quis diam. Curabitur sed arcu ut ipsum tempor molestie sed eget ipsum.</p>
      <div class="meta">Posted by: <span class="user">username details</span><span class="bar">|</span>2 hrs ago<span class="bar">|</span><span class="btn">Like</span></div></div>
    <div class="post" style="margin-top:14px"><p>Vivamus tempor feugiat felis nec fringilla. Aenean condimentum nunc ut felis pellentesque in aliquet orci pharetra. Duis pharetra pharetra est vel bibendum.</p>
      <div class="meta">Posted by: <span class="user">username details</span><span class="bar">|</span>2 hrs ago<span class="bar">|</span><span class="btn">Like</span></div></div>
  </section>

  <section class="feed right" style="left:493px">
    <div class="feed-badge"></div>
    <h2 class="feed-title">Follow us on lumora</h2>
    <div class="post"><p>Lorem ipsum dolor sit amet, consectetur adipiscing elit. Sed quis ante felis. Donec porta arcu vehicula purus hendrerit interdum. Suspendisse lacus magna ullamcorper ut aliquet rutrum</p>
      <div class="meta">Posted by: <span class="user">username details</span><span class="bar">|</span>2 hrs ago<span class="bar">|</span><span class="btn">Share</span><span class="count">0</span></div></div>
    <div class="post" style="margin-top:20px"><p>Curabitur laoreet, elit in tincidunt condimentum, massa tortor adipiscing nisl, non condimentum orci nunc quis diam. Curabitur sed arcu ut ipsum tempor molestie sed eget ipsum.</p>
      <div class="meta">Posted by: <span class="user">username details</span><span class="bar">|</span>2 hrs ago<span class="bar">|</span><span class="btn">Share</span><span class="count">0</span></div></div>
    <div class="post" style="margin-top:14px"><p>Vivamus tempor feugiat felis nec fringilla. Aenean condimentum nunc ut felis pellentesque in aliquet orci pharetra. Duis pharetra pharetra est vel bibendum.</p>
      <div class="meta">Posted by: <span class="user">username details</span><span class="bar">|</span>2 hrs ago<span class="bar">|</span><span class="btn">Share</span><span class="count">0</span></div></div>
  </section>

  <footer class="footer-nav">
    <div class="footer-head"></div>
    <div class="divider" style="left:201px"></div>
    <div class="divider" style="left:389px"></div>
    <div class="divider" style="left:589px"></div>
    <div class="divider" style="left:769px"></div>
    <div class="footer-col" style="left:34px"><h4>Home</h4><ul><li>Lorem ipsum dolor sit amet</li><li>Lorem ipsum dolor</li><li>Lorem ipsum dolor sit amet</li><li>Lorem ipsum</li></ul></div>
    <div class="footer-col" style="left:223px"><h4>About</h4><ul><li>Lorem ipsum dolor sit amet</li><li>Lorem ipsum</li><li>Lorem ipsum dolor</li><li>Lorem ipsum dolor sit</li></ul></div>
    <div class="footer-col" style="left:413px"><h4>Services</h4><ul><li>Lorem ipsum</li><li>Lorem ipsum dolor sit amet</li><li>Lorem ipsum dolor</li><li>Lorem ipsum</li></ul></div>
    <div class="footer-col" style="left:608px"><h4>Faq</h4><ul><li>Lorem ipsum dolor sit</li><li>Lorem ipsum</li><li>Lorem ipsum dolor sit</li><li>Lorem ipsum dolor sit amet</li></ul></div>
    <div class="footer-col" style="left:793px"><h4>Contact</h4><ul><li>Lorem ipsum dolor sit</li><li>Lorem ipsum dolor</li><li>Lorem ipsum dolor sit amet</li><li>Lorem ipsum</li></ul></div>
  </footer>
</div>
<p class="copyright">© 2011 Clearwell.&nbsp; All rights reserved</p>
</body>
</html>
```